I need to have a full website designed for a new consultancy business I'm trying to establish. It's called Brightpath consult. I need an English version to begin with, and then there should be a Danish version as well, but I'll translate that myself. Just be aware that I need two language versions. The consultancy field that I'm targeting is Leadership - and specialist development. I offer to facilitate corporate academies for global companies as well as specific workshops within leadership- or team development, strategy sessions, personal coaching and facilitation of D&I (Diversity and inclusion) workshops. BTW my logo is not in high resolution - I need that as well.

Target Market(s)

Larger companies that has a need for developing their inhouse leadership capabilities or that wants to develop their specialists to take on more responsibility.

Industry/Entity Type

Consultancy business

Coding

Number of Pages Required

Requirements
Must have
• Introduction site with a catch phrase. Book a meeting. Services that's beeing offered. Blog site with white papers etc. Language toggle (Danish/English). Cases/testimonials. About site. Contact site.

```html
<!DOCTYPE html>
<html lang="en">
<head>
<meta charset="utf-8">
<title>Brightpath Consult</title>
<link href="https://fonts.googleapis.com/css2?family=Poppins:ital,wght@0,300;0,400;0,500;0,600;0,700;1,400;1,600;1,700&display=swap" rel="stylesheet">
<style>
:root{
  --blue:#1f84cf;
  --blue-dark:#1a5fa8;
  --ink:#222428;
  --muted:#666b73;
  --pale:#e6f1fa;
  --footer:#1e1e1f;
  --white:#ffffff;
  --line:#d6d9dd;
}
*{margin:0;padding:0;box-sizing:border-box}
html,body{width:1200px;height:4308px;overflow:hidden}
body{font-family:'Poppins',sans-serif;color:var(--ink);background:var(--white);position:relative}
.abs{position:absolute}

/* hero */
.hero{position:absolute;left:0;top:0;width:1200px;height:677px;overflow:hidden}
.hero-photo{position:absolute;inset:0;background:linear-gradient(100deg,#2b2a29 0%,#4a4640 40%,#3a3836 70%,#1f1f20 100%)}
.hero-shade{position:absolute;inset:0;background:rgba(0,0,0,.3)}
.brand{font-weight:600;color:var(--white);font-size:30px;letter-spacing:1px;display:flex;align-items:center;gap:10px;white-space:nowrap}
.brand .mark{width:14px;height:14px;background:var(--white)}
.nav a{position:absolute;top:47px;font-size:13px;color:var(--white);text-decoration:none;font-weight:400;white-space:nowrap}
.social{width:16px;height:16px;border:1.5px solid currentColor;border-radius:50%}
.menu span{display:block;height:2px;background:var(--white);margin-bottom:5px}
.hero-title{position:absolute;left:158px;top:258px;font-size:60px;font-weight:600;color:var(--white);line-height:1.1;white-space:nowrap}
.hero-tagline{position:absolute;left:158px;top:322px;font-size:40px;font-weight:600;color:var(--white);line-height:1.1;white-space:nowrap}
.hero-text{position:absolute;left:162px;top:386px;font-size:13px;color:var(--white);line-height:1.35;width:520px}
.btn-outline{display:flex;align-items:center;justify-content:center;gap:10px;border:1.5px solid var(--ink);font-size:13px;color:var(--ink);white-space:nowrap}
.hero-btn{position:absolute;left:162px;top:440px;width:136px;height:36px;border-color:var(--white);color:var(--white)}
.circle-btn{width:34px;height:34px;border:1.5px solid rgba(255,255,255,.8);border-radius:50%;display:flex;align-items:center;justify-content:center}

/* about */
.about-title{left:162px;top:800px;font-size:60px;font-weight:500;white-space:nowrap}
.about-sub{left:172px;top:878px;font-size:15px;font-style:italic;color:var(--ink);white-space:nowrap}
.about-sub em{color:var(--blue)}
.about-text{left:546px;top:755px;width:492px;font-size:12.5px;line-height:1.6;color:var(--muted)}
.about-text p+p{margin-top:14px}

/* careers */
.careers-photo{left:546px;top:1083px;width:654px;height:417px;background:linear-gradient(120deg,#5a4a3e,#a08a76 50%,#d8ccc0)}
.play{left:857px;top:1246px;width:92px;height:92px;border-radius:50%;background:rgba(255,255,255,.85);display:flex;align-items:center;justify-content:center}
.careers{left:0;top:1148px;width:653px;height:473px;background:var(--blue);color:var(--white)}
.careers h3{position:absolute;left:160px;top:36px;font-size:40px;font-weight:500;white-space:nowrap}
.careers .lead{position:absolute;left:162px;top:92px;font-size:15px;font-style:italic;white-space:nowrap}
.steps-line{position:absolute;left:160px;top:180px;height:205px;border-left:1.5px dashed rgba(255,255,255,.7)}
.step{position:absolute;left:138px}
.step .num{position:absolute;left:0;top:0;width:44px;height:44px;border-radius:50%;background:var(--white);color:var(--ink);font-size:16px;display:flex;align-items:center;justify-content:center}
.step h4{position:absolute;left:64px;top:-2px;font-size:18px;font-weight:500;white-space:nowrap}
.step p{position:absolute;left:64px;top:26px;width:380px;font-size:11.5px;line-height:1.25}
.years{left:693px;top:1525px;display:flex;align-items:center;gap:14px}
.years b{font-size:70px;font-style:italic;font-weight:700;color:var(--blue);line-height:1}
.years span{font-size:21px;font-style:italic;color:var(--ink);line-height:1.25;font-family:Georgia,serif}

/* services */
.section-title{left:0;width:1200px;text-align:center;font-size:40px;font-weight:500}
.section-sub{left:0;width:1200px;text-align:center;font-size:14px;font-style:italic;color:var(--ink)}
.card{top:1825px;width:321px}
.card-img{position:relative;width:321px;height:431px}
.card .arrow{position:absolute;right:0;top:381px;width:52px;height:50px;background:var(--white);display:flex;align-items:center;justify-content:center}
.card .cat{margin-top:22px;font-size:11px;text-transform:uppercase}
.card .name{font-size:15px;margin-top:2px;padding-bottom:10px;border-bottom:1.5px solid #333;white-space:nowrap}

/* cases */
.case-photo{background:linear-gradient(160deg,#8b8f95,#4e5660 60%,#3b4047)}
.case-panel{background:var(--pale)}
.case-panel h5{font-size:18px;font-weight:500;color:var(--blue-dark)}
.case-panel .role{font-size:13.5px;margin-top:8px}
.case-panel p{font-size:12px;line-height:1.5;color:var(--muted);margin-top:12px;width:480px}

/* contact */
.contact-bg{top:3375px;height:510px;background:linear-gradient(180deg,#1e4f94 0%,#5d86bd 45%,#7b7f86 75%,#2f3640 100%);border-radius:6px 6px 0 0}
.form-card{left:354px;top:3302px;width:492px;height:583px;background:var(--white);box-shadow:0 10px 30px rgba(0,0,0,.06)}
.form-card .kicker{position:absolute;top:55px;width:100%;text-align:center;font-size:13px;color:var(--blue)}
.form-card h3{position:absolute;top:75px;width:100%;text-align:center;font-size:31px;font-weight:500}
.field{position:absolute;font-size:11.5px;color:#999;border-bottom:1px solid var(--line);padding-bottom:14px}
.captcha{left:50px;top:418px;width:228px;height:55px;border:1px solid #ccc;background:#f9f9f9;border-radius:3px;font-size:10.5px;display:flex;align-items:center;padding:0 12px;gap:10px}
.captcha i{width:20px;height:20px;border:2px solid #bbb;background:var(--white);border-radius:2px}
.submit{left:50px;top:493px;width:109px;height:36px;background:var(--blue);color:var(--white);font-size:13px;font-weight:500;display:flex;align-items:center;justify-content:center}

/* footer */
.footer{left:0;top:3885px;width:1200px;height:423px;background:var(--footer);color:var(--white)}
.footer h6{position:absolute;top:54px;font-size:13px;font-weight:500}
.footer ul{position:absolute;top:86px;list-style:none;font-size:12px;line-height:30px;white-space:nowrap}
.contact-row{position:absolute;left:825px;font-size:12px;display:flex;align-items:center;gap:16px;white-space:nowrap}
.copy{position:absolute;left:162px;top:314px;font-size:12px}
.legal{position:absolute;left:162px;top:339px;font-size:12px;color:var(--blue)}
.big-cta{position:absolute;right:158px;top:280px;font-size:58px;font-weight:400;line-height:1.05;text-align:right;white-space:nowrap}
</style>
</head>
<body>

<!-- hero -->
<header class="hero">
  <div class="hero-photo" role="img" aria-label="Photo of a team working together at laptops in an office"></div>
  <div class="hero-shade"></div>
  <div class="abs brand" style="left:80px;top:36px"><span class="mark"></span>BRIGHTPATH</div>
  <nav class="nav">
    <a style="left:377px">HOME</a>
    <a style="left:468px">ABOUT US</a>
    <a style="left:590px">OUR SERVICES</a>
    <a style="left:737px">CAREERS</a>
    <a style="left:850px">CONTACT US</a>
  </nav>
  <div class="abs social" style="left:978px;top:47px;color:#fff"></div>
  <div class="abs social" style="left:1015px;top:47px;color:#fff"></div>
  <div class="abs social" style="left:1055px;top:47px;color:#fff"></div>
  <div class="abs menu" style="left:1116px;top:51px;width:26px"><span></span><span style="width:18px;margin-left:8px"></span></div>
  <h1 class="hero-title">Brightpath Consult</h1>
  <h2 class="hero-tagline">Grow Your Business With Us</h2>
  <p class="hero-text">We aim to make leadership growth easy for you! We will find the right<br>path and take care of coordinating all the support your team needs.</p>
  <div class="btn-outline hero-btn">Learn More</div>
  <div class="abs circle-btn" style="left:1110px;top:320px"><svg width="12" height="14" viewBox="0 0 12 14"><path d="M6 13V1M1 6l5-5 5 5" stroke="#fff" fill="none" stroke-width="1.3"/></svg></div>
  <div class="abs circle-btn" style="left:1110px;top:370px"><svg width="12" height="14" viewBox="0 0 12 14"><path d="M6 1v12M1 8l5 5 5-5" stroke="#fff" fill="none" stroke-width="1.3"/></svg></div>
</header>

<!-- about -->
<div class="abs about-title">About Us</div>
<div class="abs about-sub">We Built trust in our <em>customer's mind...</em></div>
<div class="abs about-text">
  <p>We at Brightpath Consult believe that people are the future. We also believe that resistance to new ways of leading, whether personal or corporate, slows progress. As a result, we assist businesses in identifying and meeting the demand for strong leadership by delivering academies and consulting services that promote competitiveness and innovation.</p>
  <p>Our headquarters is based in Copenhagen, Denmark. However, our team is mainly remote. We pride ourselves on working well as a team and with our clients alike. We are experienced in remote team collaboration and facilitation, we painlessly integrate into globally distributed multi-site teams.</p>
</div>
<div class="abs btn-outline" style="left:546px;top:976px;width:138px;height:37px">Learn More <svg width="9" height="9" viewBox="0 0 9 9"><path d="M1 8l7-7M3 1h5v5" stroke="#222" fill="none"/></svg></div>

<!-- careers -->
<div class="abs careers-photo" role="img" aria-label="Photo of three colleagues smiling around a laptop"></div>
<div class="abs play"><svg width="26" height="28" viewBox="0 0 26 28"><path d="M2 1l22 13L2 27z" fill="#1f84cf"/></svg></div>
<section class="abs careers">
  <h3>Careers &amp; Hiring</h3>
  <div class="lead">We are building great future Together, Be with us...</div>
  <div class="steps-line"></div>
  <div class="step" style="top:153px"><div class="num">1</div><h4>Why work for Brightpath?</h4><p>Giving consultancy for every leadership development programme and analysis for existing project.</p></div>
  <div class="step" style="top:259px"><div class="num">2</div><h4>Opportunities</h4><p>Giving consultancy for every leadership development programme and analysis for existing project.</p></div>
  <div class="step" style="top:366px"><div class="num">3</div><h4>Graduate Opportunities</h4><p>Giving consultancy for every leadership development programme and analysis for existing project.</p></div>
</section>
<div class="abs years"><b>10</b><span>Years of<br>Experience</span></div>

<!-- services -->
<div class="abs section-title" style="top:1700px">Our Services</div>
<div class="abs section-sub" style="top:1757px">We are building great future Together, Be with us</div>
<div class="abs card" style="left:94px">
  <div class="card-img" role="img" aria-label="Photo of two colleagues reviewing work at a desk" style="background:linear-gradient(150deg,#e8eaec,#b9c3cf 50%,#2b3e63)">
    <div class="arrow"><svg width="30" height="12" viewBox="0 0 30 12"><path d="M0 6h28M23 1l5 5-5 5" stroke="#222" fill="none" stroke-width="1.3"/></svg></div>
  </div>
  <div class="cat">Business</div><div class="name">Corporate Academies</div>
</div>
<div class="abs card" style="left:439px">
  <div class="card-img" role="img" aria-label="Photo of two professionals looking at a tablet" style="background:linear-gradient(150deg,#f1f2f3,#a9b0ba 50%,#2a3550)">
    <div class="arrow"><svg width="30" height="12" viewBox="0 0 30 12"><path d="M0 6h28M23 1l5 5-5 5" stroke="#222" fill="none" stroke-width="1.3"/></svg></div>
  </div>
  <div class="cat">Business</div><div class="name">Specialist Development</div>
</div>
<div class="abs card" style="left:785px">
  <div class="card-img" role="img" aria-label="Photo of a consultant working at a laptop by a window" style="background:linear-gradient(150deg,#eef0f1,#c4c8cc 50%,#3d4149)">
    <div class="arrow"><svg width="30" height="12" viewBox="0 0 30 12"><path d="M0 6h28M23 1l5 5-5 5" stroke="#222" fill="none" stroke-width="1.3"/></svg></div>
  </div>
  <div class="cat">Business</div><div class="name">Leadership Coaching</div>
</div>
<div class="abs btn-outline" style="left:515px;top:2376px;width:169px;height:37px;font-size:12.5px">View All Services <svg width="9" height="9" viewBox="0 0 9 9"><path d="M1 8l7-7M3 1h5v5" stroke="#222" fill="none"/></svg></div>

<!-- cases -->
<div class="abs section-title" style="top:2486px">Case Studies &amp; Success Stories</div>
<div class="abs section-sub" style="top:2545px">We are building great future Together, Be with us</div>
<div class="abs case-panel" style="left:438px;top:2637px;width:600px;height:209px;padding:38px 0 0 38px">
  <h5>MARTIN HALE</h5>
  <div class="role">Founder and Principal Leadership Development Consultant</div>
  <p>Martin has a doctorate in organisational psychology and more than 20 years of experience in the pharmaceutical and biotechnology industries. During his career, he has led EU, US, and UK leadership projects in industry and consulting.</p>
</div>
<div class="abs case-photo" role="img" aria-label="Portrait photo of a male consultant" style="left:160px;top:2608px;width:278px;height:266px"></div>
<div class="abs case-panel" style="left:160px;top:2948px;width:602px;height:207px;padding:38px 0 0 38px">
  <h5>CLARA WENDT</h5>
  <div class="role">Expert Team Development Consultant</div>
  <p>Clara has a doctorate in organisational psychology and more than 20 years of experience in the pharmaceutical and biotechnology industries. During her career, she has led EU, US, and UK leadership projects in industry and consulting.</p>
</div>
<div class="abs case-photo" role="img" aria-label="Portrait photo of a female consultant" style="left:762px;top:2919px;width:276px;height:264px;background:linear-gradient(160deg,#e6e1da,#c9b59a 55%,#9d8a78)"></div>

<!-- contact -->
<div class="abs contact-bg" role="img" aria-label="Photo of a modern angular building under a blue sky" style="left:22px;width:1156px"></div>
<div class="abs form-card">
  <div class="kicker">Contact</div>
  <h3>Get In Touch</h3>
  <div class="field" style="left:50px;top:145px;width:176px">Name*</div>
  <div class="field" style="left:266px;top:145px;width:177px">Company Name</div>
  <div class="field" style="left:50px;top:207px;width:176px">Phone</div>
  <div class="field" style="left:266px;top:207px;width:177px">Email Address*</div>
  <div class="field" style="left:50px;top:269px;width:393px">State</div>
  <div class="field" style="left:50px;top:330px;width:393px;height:67px">Your Message</div>
  <div class="abs captcha"><i></i>I'm not a robot</div>
  <div class="abs submit">SUBMIT</div>
</div>

<!-- footer -->
<footer class="abs footer">
  <div class="abs brand" style="left:160px;top:120px;font-size:36px"><span class="mark"></span>BRIGHTPATH</div>
  <h6 style="left:416px">Quick Links</h6>
  <ul style="left:416px"><li>Home</li><li>Who We Are</li><li>Our Process</li><li>Schedule A Demo</li><li>Contact Us</li></ul>
  <h6 style="left:580px">Services</h6>
  <ul style="left:580px"><li>Corporate Academies</li><li>Specialist Development</li><li>Leadership Coaching</li><li>Team Development</li><li>Workshops &amp; Facilitation</li></ul>
  <h6 style="left:819px">Contact Us</h6>
  <div class="contact-row" style="top:86px"><svg width="14" height="14" viewBox="0 0 24 24"><path d="M6.6 10.8a15 15 0 006.6 6.6l2.2-2.2a1 1 0 011-.25 11.4 11.4 0 003.6.57 1 1 0 011 1V20a1 1 0 01-1 1A17 17 0 013 4a1 1 0 011-1h3.5a1 1 0 011 1c0 1.25.2 2.45.57 3.57a1 1 0 01-.25 1z" fill="#fff"/></svg>0700 000 1234</div>
  <div class="contact-row" style="top:114px"><svg width="14" height="11" viewBox="0 0 14 11"><rect x=".5" y=".5" width="13" height="10" fill="none" stroke="#fff"/><path d="M.5.5l6.5 5 6.5-5" fill="none" stroke="#fff"/></svg>hello@brightpath-consult.example</div>
  <div class="abs" style="left:819px;top:152px;width:218px;border-top:1px solid #777"></div>
  <div class="abs social" style="left:824px;top:170px;color:#fff"></div>
  <div class="abs social" style="left:866px;top:170px;color:#fff"></div>
  <div class="abs social" style="left:908px;top:170px;color:#fff"></div>
  <div class="copy">Copyright 2012 - 2025 Brightpath Consult Limited</div>
  <div class="legal">Terms &amp; Conditions &nbsp; - &nbsp; Privacy Policy</div>
  <div class="big-cta">Get In<br>Touch <svg width="40" height="40" viewBox="0 0 40 40"><path d="M3 37L37 3M12 3h25v25" stroke="#fff" fill="none" stroke-width="2"/></svg></div>
</footer>

</body>
</html>
```